Web Button design and production

I need remote control like buttons (or your own design of buttons if I like it)
3x4 text buttons (normal, pressed, disabled)
3x1 empty button (normal, pressed, disabled)
3x6 buttons with glyph (normal, pressed, disabled)
3x288 with 24h time "00:00", "00:05", "00:10" (normal, pressed, disabled)
4 LED (red, green, orange, black)
I will upload the background image as soon as possible (black plastic)
See attached images
Q: Do the buttons have to be gray/black?
A: It should look like a high end remote control. It could be brushed aluminum as well, or something you come up with. But I guess black or dark grey would be best. The background will be picsharbor 40561739, but it's not available yet.
Q: Do I have to provide all buttons for the contest?
A: No! I only need one button (3 states) and a LED to decide. Only the winner will do the whole job.
Q: Is the Designer who wins the contest expected to complete all the extra buttons?
A: Yes, please.
Plastic

```html
<!DOCTYPE html>
<html lang="en">
<head>
<meta charset="utf-8">
<title>Remote Control Button States</title>
<link rel="stylesheet" href="https://fonts.googleapis.com/css2?family=Arimo:wght@400;700&display=swap">
<style>
  :root {
    --page: #ffffff;
    --label: #111111;
    --slate-top: #5a5a5a;
    --slate-mid: #3a3a3a;
    --slate-low: #262626;
    --slate-text-dim: #6e6e6e;
    --slate-text: #e8e8e8;
    --frame: #050505;
    --steel-top: #8a8a8a;
    --steel-low: #2e2e2e;
    --tan-top: #e6cfa6;
    --tan-low: #b8976a;
    --olive-top: #9c8a6a;
    --olive-low: #5e4f36;
    --amber-top: #e2a96a;
    --amber-low: #b0723a;
    --brown-text: #2a1a08;
    --pill-top: #fbfbfb;
    --pill-low: #d4d4d4;
    --pill-border: #b8b8b8;
    --ink: #111111;
    --alert: #9a0d0d;
  }
  html, body {
    margin: 0; padding: 0; overflow: hidden;
    background: var(--page);
  }
  .sheet {
    position: relative; width: 1200px; height: 720px; overflow: hidden;
    font-family: "Arimo", Arial, sans-serif;
  }
  .state-label {
    position: absolute; right: 1000px; margin: 0;
    font-size: 44px; color: var(--label); line-height: 1;
  }
  .btn {
    position: absolute; display: flex; align-items: center; justify-content: center;
    box-sizing: border-box; font-family: "Arimo", Arial, sans-serif;
  }
  /* Slate buttons */
  .slate {
    width: 138px; height: 105px; border-radius: 8px;
    background: linear-gradient(180deg, var(--slate-top) 0%, var(--slate-mid) 45%, var(--slate-low) 100%);
    box-shadow: 0 5px 10px rgba(0,0,0,.45), inset 0 2px 2px rgba(255,255,255,.25);
    font-size: 48px;
  }
  .slate.engraved { color: var(--slate-text-dim); text-shadow: -1px -1px 1px rgba(0,0,0,.7), 1px 1px 1px rgba(255,255,255,.15); }
  .slate.lit { color: var(--slate-text); }
  .slate.pressed { background: linear-gradient(180deg, #6a6a6a, #474747); box-shadow: 0 3px 12px rgba(0,0,0,.35), inset 0 0 10px rgba(0,0,0,.3); }
  .slate.disabled { background: linear-gradient(180deg, #4a4a4a, #1c1c1c); color: #555; }
  .slate.lit.disabled { color: #d0d0d0; }
  /* Framed steel buttons */
  .frame {
    position: absolute; background: var(--frame); border-radius: 4px; padding: 10px; box-sizing: border-box;
  }
  .frame .btn { position: static; width: 100%; height: 100%; border-radius: 6px; }
  .steel-frame { width: 178px; height: 118px; }
  .steel {
    background: linear-gradient(180deg, var(--steel-top) 0%, #555 40%, var(--steel-low) 100%);
    box-shadow: inset 0 2px 2px rgba(255,255,255,.45);
    color: #f4f4f4; font-weight: 700; font-size: 50px;
  }
  .steel.pressed { background: linear-gradient(180deg, #444, #141414); color: #e8e8e8; }
  .steel.disabled { background: linear-gradient(180deg, #b4b4b4, #7a7a7a); color: #e6e6e6; }
  /* Framed tan buttons */
  .tan-frame { width: 223px; height: 145px; padding: 12px; }
  .tan {
    font-weight: 700; font-size: 62px; color: var(--brown-text);
    box-shadow: inset 0 3px 3px rgba(255,255,255,.5), inset 0 -3px 4px rgba(0,0,0,.25);
    border-radius: 10px;
  }
  .tan.normal { background: linear-gradient(180deg, var(--tan-top), var(--tan-low)); }
  .tan.pressed { background: linear-gradient(180deg, var(--olive-top), var(--olive-low)); }
  .tan.disabled { background: linear-gradient(180deg, var(--amber-top), var(--amber-low)); }
  /* Pill buttons */
  .pill {
    top: 548px; width: 205px; height: 127px; border-radius: 16px;
    border: 2px solid var(--pill-border);
    background: linear-gradient(180deg, var(--pill-top), var(--pill-low));
    box-shadow: 0 6px 10px rgba(0,0,0,.2);
    font-weight: 700; font-size: 62px; color: var(--ink);
  }
  .pill.pressed { background: linear-gradient(180deg, #6a6a6a 0%, #bdbdbd 55%, #f2f2f2 100%); padding-top: 14px; }
  .pill.alert { color: var(--alert); font-weight: 400; }
</style>
</head>
<body>
<main class="sheet">
  <p class="state-label" style="top:60px">Normal</p>
  <p class="state-label" style="top:222px">Pressed</p>
  <p class="state-label" style="top:368px">Disable</p>

  <div class="btn slate engraved" style="left:232px;top:33px">80</div>
  <div class="btn slate engraved pressed" style="left:232px;top:192px">80</div>
  <div class="btn slate engraved disabled" style="left:232px;top:335px">80</div>

  <div class="btn slate lit" style="left:457px;top:33px">80</div>
  <div class="btn slate lit pressed" style="left:457px;top:192px">80</div>
  <div class="btn slate lit disabled" style="left:457px;top:335px">80</div>

  <div class="frame steel-frame" style="left:682px;top:30px"><div class="btn steel">00</div></div>
  <div class="frame steel-frame" style="left:682px;top:187px"><div class="btn steel pressed">00</div></div>
  <div class="frame steel-frame" style="left:682px;top:332px"><div class="btn steel disabled">00</div></div>

  <div class="frame tan-frame" style="left:937px;top:22px"><div class="btn tan normal">800</div></div>
  <div class="frame tan-frame" style="left:937px;top:192px"><div class="btn tan pressed">800</div></div>
  <div class="frame tan-frame" style="left:937px;top:374px"><div class="btn tan disabled">800</div></div>

  <div class="btn pill" style="left:205px">50</div>
  <div class="btn pill pressed" style="left:480px">50</div>
  <div class="btn pill alert" style="left:745px">50</div>
</main>
</body>
</html>
```